PLUM- company with a mission

PLUM LLC stands for pure living under moonlight (non profit arm is called bright lantern foundation)—our business is based out of New York City and has a non-profit arm where for every bar you purchase, we donate a bar (don’t want any designs that limits us to only soap). Currently working with South Africa. We want the focus to be organic/natural soap with a mission.
What our website needs to…achieve:
Purpose = branding, building up interesting leaving up to launch date, then a full functional site for selling soap (for now) with a mission. With that said, there will need to be a page designed for “COMING SOON” – with a place to post our teaser 30 second video (kind of like a commercial/movie trailer) – until everything else is done.
We are the first in the industry to do one for one (or …50/50). Most companies that do charity work are mostly for every $$$ we donate $0.10, or 1% of XXX. We are starting out to run the non-profit arm as well not just after we reach certain milestones. In addition, we will be transparent for the non-profit side whereas most of the time when you donate, you have no idea where the money ends up going.
IN ADDITION: we still need to be clean/elegant – and selling our soap; so website will need to 1. Showcase our products, 2. Be very clear that we have a mission (not sure if there is a way to show case both our soap AND our mission)
Some sites we like:
Velbrook.com—like them in terms of business model—in terms of their website: like how their site is clean and friendly, but it seems too cluttered
www.quindelmarsh.com -- similar business model, www.pemaroux.com, kelvashop.com, ridgelybar.com
Duvik.com: like this a lot better than fernwicke.com, however, major dislike of the typeface. Okay about the neutral colors…although feel like we need something a bit more cheerful here and there for our mission
Zlabel.net, kelvashop.com, castlewren.com: like how they are clean and showcase well
**** However, our site also needs to convey messages like: www.feverfreeworld.org, www.cleanhandsunited.org
Looking for a clean, simple design. Modern, clutter-free, and inviting. Definitely do not want an arts and crafty/flowery feel. We do need something…cheerful for our nonprofit purposes.
Examples of sites we don’t like: marigoldhaus.com, petalpressbar.com
7 pages/ tabs maybe? (About us…video page (to show case what we are doing –currently my partner is in South Africa filming what our mission will be able to do – give children and those in need soap), FAQs, soap products, terms & conditions, contact us page, blog page……nothing too crazy).
For now, for designing purposes, please use any example texts whether it’s the about us page, mission page..policies.. and for the soap/products pages—please use example you can find online – it is fine, we just need the design done for now.
I have also attached our logo file. Please let me know if you have any questions! Thanks!
Something to consider....
velbrook.com and quindelmarsh.com are probably our largest competitor out of all the websites I mentioned as they have a very similar business model where it is is a company with a mission. Homepage makes that clear that for every pair of shoes/ glasses you purchase, they give a pair. Another thing to note...is that they have been in business for a few years so their website probably have changed to more commercial than focusing/marketing on the mission of doing good. While we don't want that to be the total focus, we do need it to be present on the homepage/front page.
Non-Profit

```html
<!DOCTYPE html>
<html lang="en">
<head>
<meta charset="utf-8">
<title>PLUM — One Soap Makes One Child Save</title>
<link rel="stylesheet" href="https://fonts.googleapis.com/css2?family=Questrial&family=Open+Sans:wght@400;600&display=swap">
<style>
:root{
  --orange:#ef8a3a;
  --orange-light:#f4a55c;
  --orange-deep:#e8742a;
  --teal:#18a9b8;
  --ink:#222;
  --text:#555;
  --muted:#8a8a8a;
  --line:#dcdcdc;
  --grey-band:#efefef;
  --white:#fff;
}
*{box-sizing:border-box;margin:0;padding:0}
html,body{width:1200px;height:2236px;overflow:hidden;background:var(--white)}
body{font-family:"Open Sans",sans-serif;color:var(--text);position:relative}
.abs{position:absolute}
.display{font-family:"Questrial",sans-serif}

/* header */
.utility{top:10px;right:134px;font-size:15px;color:#444;font-family:"Questrial",sans-serif;word-spacing:2px}
.social-top{top:62px;left:948px;display:flex;gap:3px}
.dot{width:28px;height:28px;border-radius:50%;background:#5b5b5b}
.nav{top:109px;left:0;width:1200px;height:56px;background:linear-gradient(var(--orange-light),var(--orange-deep))}
.nav a{position:absolute;top:0;height:56px;line-height:56px;color:var(--white);text-decoration:none;font-family:"Questrial",sans-serif;font-size:19px;padding:0 0}
.nav .sep{position:absolute;top:0;width:1px;height:56px;background:rgba(255,255,255,.35)}
.brand{top:28px;left:525px;width:164px;height:164px;border-radius:50%;background:var(--orange-light);border:6px solid var(--white);display:flex;align-items:center;justify-content:center;color:var(--white);font-family:"Questrial",sans-serif;font-size:40px;letter-spacing:2px}

/* hero */
.hero{top:165px;left:0;width:1200px;height:446px;background:linear-gradient(100deg,#e2eddb 0%,#dbe8cf 45%,#c9d9b3 65%,#e6cfd6 100%)}
.hero-title{top:270px;left:117px;font-size:46px;color:var(--orange)}
.hero-sub{top:326px;left:117px;font-size:33px;color:var(--ink)}
.hero-copy{top:373px;left:122px;width:370px;font-size:12.5px;line-height:19px;color:#444}
.pager{top:422px;left:121px;display:flex;gap:3px}
.pager span{width:11px;height:11px;border-radius:50%;background:#888}
.pager span:first-child{background:#111}

/* intro */
.intro{top:662px;left:0;width:1200px;text-align:center}
.intro h1{font-family:"Questrial",sans-serif;font-weight:400;font-size:33px;color:#333}
.intro h2{font-family:"Questrial",sans-serif;font-weight:400;font-size:21px;color:#777;margin-top:6px}
.intro p{width:972px;margin:18px auto 0;font-size:12.5px;line-height:19px;color:#777}
.donate-btn{top:818px;left:517px;width:164px;height:44px;background:linear-gradient(var(--orange-light),var(--orange));color:var(--white);font-family:"Questrial",sans-serif;font-size:17px;line-height:44px;text-align:center}

/* products */
.product{width:310px}
.product .frame{height:164px;border:1px solid var(--line);background:var(--white);display:flex;align-items:center;justify-content:center}
.product .frame div{width:86%;height:80%;border-radius:6px}
.product h3{font-family:"Questrial",sans-serif;font-weight:400;font-size:24px;color:var(--teal);margin-top:8px}
.product p{font-size:12.5px;line-height:19px;color:#777;margin-top:2px}

/* stories band */
.band{top:1518px;left:0;width:1200px;height:393px;background:var(--grey-band)}
.story{top:1565px;left:116px;width:406px;height:288px;background:var(--white);border:1px solid var(--line)}
.story .photo{height:191px;background:linear-gradient(135deg,#8d7a64,#b9a58a 50%,#6d6152)}
.story h3{font-family:"Questrial",sans-serif;font-weight:400;font-size:20px;color:var(--orange);margin:14px 0 0 24px}
.story p{font-size:11.5px;line-height:17px;color:#888;margin:4px 20px 0 24px}
.mono{top:1565px;left:532px;width:233px;height:288px;background:linear-gradient(150deg,#5a5a5a,#b4b4b4 55%,#3c3c3c)}
.recent{top:1565px;left:765px;width:319px;height:288px;background:var(--white);border:1px solid var(--line);padding:24px 26px}
.recent h3{font-family:"Questrial",sans-serif;font-weight:400;font-size:24px;color:#111}
.recent p{font-size:11.5px;line-height:17px;color:#888}
.recent .lead{margin-top:8px}
.recent h4{font-weight:400;font-size:12.5px;color:#222;margin-top:12px}
.recent .more{display:block;margin-top:10px;font-size:11.5px;color:var(--orange);text-transform:uppercase}

/* footer */
.footer{top:1911px;left:0;width:1200px;height:325px;background:linear-gradient(#f0a55c,#e66f25)}
.col{top:1960px;color:var(--white)}
.col h4{font-family:"Questrial",sans-serif;font-weight:400;font-size:21px;text-transform:uppercase;margin-bottom:6px}
.col li{list-style:none;font-size:13px;line-height:24px}
.col p{font-size:13px;line-height:24px}
.signup{margin-top:8px;display:flex}
.signup .field{width:243px;height:34px;background:var(--white);color:#999;font-size:12px;line-height:34px;padding-left:14px}
.signup .submit{width:85px;height:34px;background:#111;color:var(--white);font-size:13px;font-weight:600;line-height:34px;text-align:center}
.social-foot{display:flex;gap:4px;margin-top:12px}
.social-foot span{width:28px;height:28px;border-radius:50%;border:2px solid var(--white)}
.rule{top:2176px;left:116px;width:968px;height:1px;background:rgba(255,255,255,.45)}
.legal{top:2200px;left:116px;font-size:12px;color:var(--white)}
</style>
</head>
<body>

<header>
  <div class="abs utility">Help &nbsp;/&nbsp; Login &nbsp;/&nbsp; Cart &nbsp;/&nbsp; Donate</div>
  <div class="abs social-top"><span class="dot"></span><span class="dot"></span><span class="dot"></span><span class="dot"></span></div>
  <nav class="abs nav">
    <a href="#" style="left:127px">About us</a><span class="sep" style="left:209px"></span>
    <a href="#" style="left:221px">Our Mission</a><span class="sep" style="left:324px"></span>
    <a href="#" style="left:338px">FAQ</a><span class="sep" style="left:385px"></span>
    <a href="#" style="left:400px">Soap products</a>
    <a href="#" style="left:700px">Terms &amp; Conditions</a><span class="sep" style="left:860px"></span>
    <a href="#" style="left:876px">Contact us</a><span class="sep" style="left:970px"></span>
    <a href="#" style="left:985px">Blog page</a>
  </nav>
  <div class="abs brand">PLUM</div>
</header>

<section class="abs hero" role="img" aria-label="Photo of a young girl in a grassy field holding out a bar of soap"></section>
<div class="abs hero-title display">One Soap Makes</div>
<div class="abs hero-sub display">One Child Save</div>
<p class="abs hero-copy">Aendum accumsan vestibulum ut commodo a mi Morbi ornare gravida elit Integer congue augue malesuada</p>
<div class="abs pager"><span></span><span></span><span></span><span></span></div>

<section class="abs intro">
  <h1>There are a lot of ways that you can help.</h1>
  <h2>Duis quam Nam eget lacus Aliquam erat volutpat Quisque dignissim congue leo</h2>
  <p>Aliquam nec erat at purus cursus interdum Vestibulum ligula augue bibendum accumsan vestibulum ut commodo a mi Morbi ornare gravida elit Integer congue augue et malesuada iaculis ipsum dui aliquet felis at cursus magna nisl nec elit Vestibulum gravida Praesent elementum elit at tellus Malesuada nec ultricies sit amet porttitor mattis enim In massa libero interdum nec interdum vel blandit sed nulla In ullamcorper est eget tempor cursus</p>
</section>
<div class="abs donate-btn">DONATE NOW</div>

<article class="abs product" style="top:923px;left:116px">
  <div class="frame"><div role="img" aria-label="Stacked natural soap bars with green leaves" style="background:linear-gradient(90deg,#efe6cf,#d8c9a4,#6d9b4a)"></div></div>
  <h3>Featured Product</h3><p>Aliquam nec erat at purus cursus interdum Vestibu-lum ligula augue bibendum accumsan</p>
</article>
<article class="abs product" style="top:923px;left:446px">
  <div class="frame"><div role="img" aria-label="Handmade soap bars with lavender sprigs" style="background:linear-gradient(90deg,#e4dcc4,#cdbf9a,#d9cfb4)"></div></div>
  <h3>Featured Product</h3><p>Aliquam nec erat at purus cursus interdum Vestibu-lum ligula augue bibendum accumsan</p>
</article>
<article class="abs product" style="top:923px;left:774px">
  <div class="frame"><div role="img" aria-label="Stack of pastel soap bars and a round soap" style="background:linear-gradient(90deg,#e3b07e,#f2eadc,#a9b97a)"></div></div>
  <h3>Featured Product</h3><p>Aliquam nec erat at purus cursus interdum Vestibu-lum ligula augue bibendum accumsan</p>
</article>
<article class="abs product" style="top:1207px;left:116px">
  <div class="frame"><div role="img" aria-label="Amber glycerin soap bar" style="background:linear-gradient(135deg,#e8a469,#b8642c)"></div></div>
  <h3>Featured Product</h3><p>Aliquam nec erat at purus cursus interdum Vestibu-lum ligula augue bibendum accumsan</p>
</article>
<article class="abs product" style="top:1207px;left:446px">
  <div class="frame"><div role="img" aria-label="Cream coloured branded soap bar" style="background:linear-gradient(135deg,#f6f1e3,#e1d7c0)"></div></div>
  <h3>Featured Product</h3><p>Aliquam nec erat at purus cursus interdum Vestibu-lum ligula augue bibendum accumsan</p>
</article>
<article class="abs product" style="top:1207px;left:774px">
  <div class="frame"><div role="img" aria-label="Bright orange translucent soap bar" style="background:linear-gradient(135deg,#ffb070,#f06a1c)"></div></div>
  <h3>Featured Product</h3><p>Aliquam nec erat at purus cursus interdum Vestibu-lum ligula augue bibendum accumsan</p>
</article>

<section class="abs band"></section>
<article class="abs story">
  <div class="photo" role="img" aria-label="Photo of three young children sitting together outdoors"></div>
  <h3>HOW WE DONATE</h3>
  <p>Aliquam nec erat at purus cursus interdum Vestibulum ligula augue bibendum accumsan vestibulum ut commodo</p>
</article>
<div class="abs mono" role="img" aria-label="Black and white photo of children in a community"></div>
<aside class="abs recent">
  <h3>RECENT POST</h3>
  <p class="lead">Maecenas at justo id velit placerat molestie Donec dictum lectus non odio Cras a ante vitae enim iaculis aliquam Mauris nunc quam venenatis nec euismod sit amet egestas placerat</p>
  <h4>Maecenas at justo id velit</h4><p>Mauris nunc quam venenatis nec euismod.</p>
  <h4>Pellentesque faucibus</h4><p>Pellentesque habitant morbi tristique senectus</p>
  <a class="more">View more blog post</a>
</aside>

<footer class="abs footer"></footer>
<div class="abs col" style="left:127px"><h4>Quick Links</h4><ul><li>Etiam eu urna</li><li>Suspendisse quam</li><li>Leo molestie sed</li><li>Geugiat pede</li><li>Fusce tellus Sed</li></ul></div>
<div class="abs col" style="left:335px"><h4>Features</h4><ul><li>Etiam eu urna</li><li>Suspendisse quam</li><li>Leo molestie sed</li><li>Geugiat pede</li><li>Fusce tellus Sed</li></ul></div>
<div class="abs col" style="left:534px"><h4>Products</h4><ul><li>Etiam eu urna</li><li>Suspendisse quam</li><li>Leo molestie sed</li><li>Geugiat pede</li><li>Fusce tellus Sed</li></ul></div>
<div class="abs col" style="left:726px"><h4>Newsletters</h4><p>Please sign up here for latest offers.</p>
  <div class="signup"><div class="field">email address</div><div class="submit">SUBMIT</div></div>
  <div class="social-foot"><span></span><span></span><span></span><span></span></div>
</div>
<div class="abs rule"></div>
<div class="abs legal">© 2014 Company Name &nbsp;All right reserved &nbsp;Term of Use</div>

</body>
</html>
```